Singapore Peer-to-Peer Business Loans Site Needs a Name Card Design

We need a name card design for a new company based in Singapore called 'Ledgerbridge Capital (Singapore) Pte. Ltd.' or in short, 'LedcapSG'.
We run an online platform where small and medium enterprises can access seed capital from wealthy persons seeking high yield returns.
We need a name card design - We would like to see designs that use the colours red, black and/or grey, using any combination of the logos that we have attached. The final design should communicate transparency, innovativeness, financial savvy, and professionalism.
Target Market(s)
Sophisticated/expert financial investors and small & medium business owners.
Industry/Entity Type
Financial
Look and feel
Each slider illustrates characteristics of the customer's brand and the style your logo design should communicate.

```html
<!DOCTYPE html>
<html lang="en">
<head>
<meta charset="utf-8">
<title>LedcapSG Name Card</title>
<link rel="stylesheet" href="https://fonts.googleapis.com/css2?family=Jost:wght@400;600;700&display=swap">
<style>
  :root {
    --brand-red: #e52629;
    --card-grey: #d1d2d4;
    --ink: #111111;
    --paper: #ffffff;
  }
  * { margin: 0; padding: 0; box-sizing: border-box; }
  html, body {
    width: 911px;
    height: 1200px;
    overflow: hidden;
    background: var(--paper);
    font-family: "Jost", "Century Gothic", sans-serif;
    color: var(--ink);
  }
  .sheet { position: relative; width: 911px; height: 1200px; }
  .side-label {
    position: absolute;
    left: 0;
    font-size: 21px;
    font-weight: 400;
    letter-spacing: 0.5px;
  }
  .side-label--back { top: -4px; left: 8px; }
  .side-label--front { top: 660px; }

  .card {
    position: absolute;
    left: 3px;
    width: 870px;
    height: 497px;
  }
  .card--back { top: 35px; background: var(--card-grey); }
  .card--front { top: 696px; background: var(--brand-red); }

  .brand-lockup {
    position: absolute;
    display: flex;
    align-items: center;
  }
  .brand-square { display: block; flex: none; }
  .brand-name { white-space: nowrap; line-height: 1; }

  .card--back .brand-lockup { left: 72px; top: 78px; gap: 12px; }
  .card--back .brand-square { width: 26px; height: 26px; background: var(--brand-red); }
  .card--back .brand-name { font-size: 64px; font-weight: 400; color: var(--brand-red); }

  .holder-name {
    position: absolute;
    left: 64px;
    top: 250px;
    font-size: 47px;
    font-weight: 400;
    letter-spacing: 0.5px;
  }
  .contact {
    position: absolute;
    left: 0;
    width: 870px;
    top: 378px;
    text-align: center;
    font-size: 22.5px;
    line-height: 31px;
  }
  .contact strong { font-weight: 700; }
  .contact .accent { color: var(--brand-red); font-weight: 700; }
  .contact .divider { color: var(--brand-red); margin: 0 10px; }

  .card--front .brand-lockup {
    left: 50%;
    top: 50%;
    transform: translate(-50%, -50%);
    gap: 20px;
  }
  .card--front .brand-square { width: 40px; height: 40px; background: var(--paper); }
  .card--front .brand-name { font-size: 104px; font-weight: 600; color: var(--paper); letter-spacing: -1px; }
</style>
</head>
<body>
<main class="sheet">
  <p class="side-label side-label--back">BACK</p>
  <section class="card card--back" aria-label="Card back">
    <div class="brand-lockup">
      <span class="brand-square"></span>
      <span class="brand-name">LedcapSG</span>
    </div>
    <h1 class="holder-name">MARCUS ONG</h1>
    <address class="contact" style="font-style:normal">
      <div>18 Harbour Lane, #14-00 Meridian Tower, Singapore 049317</div>
      <div>Direct <span class="accent">+</span> <strong>65 6420 5170</strong><span class="divider">|</span><strong>hello</strong>@ledcap.sg<span class="divider">|</span>www.<strong>ledcap</strong>.sg</div>
    </address>
  </section>

  <p class="side-label side-label--front">FRONT</p>
  <section class="card card--front" aria-label="Card front">
    <div class="brand-lockup">
      <span class="brand-square"></span>
      <span class="brand-name">LedcapSG</span>
    </div>
  </section>
</main>
</body>
</html>
```